tqbarlowstudio website

I need a new homepage design for my current website at www.TQBarlowStudio.com. I want someone to look at my current website and develop a more appealing homepage... right now the colors don't blend very well and it needs a facelift

```html
<!DOCTYPE html>
<html lang="en">
<head>
<meta charset="utf-8">
<title>TQ Barlow – Home</title>
<link href="https://fonts.googleapis.com/css2?family=Lato:wght@300;400;700&family=Questrial&display=swap" rel="stylesheet">
<style>
:root{
  --bar:#242424;
  --nav:#1d1d1d;
  --hero:#3e302e;
  --hero-dark:#2f2523;
  --tan:#a9825a;
  --gold:#b08d5e;
  --ink:#ffffff;
  --muted:#9a9a9a;
  --green-deep:#2b3a12;
  --green-mid:#6f8f2c;
  --green-light:#b7c97a;
  --tick:#8cc83c;
  --panel:rgba(20,22,16,.82);
  --white:#ffffff;
  --footer:#222222;
}
*{box-sizing:border-box;margin:0;padding:0}
html,body{width:792px;height:1200px;overflow:hidden;background:var(--white)}
body{font-family:"Lato",sans-serif;color:var(--ink);position:relative}
.topbar{position:absolute;top:0;left:0;width:792px;height:56px;background:var(--bar);border-bottom:1px solid #3a3a3a}
.brand{position:absolute;left:0;width:792px;top:8px;text-align:center;font-family:"Questrial",sans-serif;font-size:32px;letter-spacing:2px;color:var(--gold)}
.social{position:absolute;right:136px;top:17px;display:flex;gap:8px}
.social span{width:18px;height:18px;border-radius:50%;background:#6e6e6e;display:block}
.mainnav{position:absolute;top:57px;left:0;width:792px;height:39px;background:var(--nav);display:flex;justify-content:center;gap:0}
.mainnav a{font-family:"Questrial",sans-serif;font-size:11.5px;color:var(--muted);text-decoration:none;line-height:36px;padding:0 11px;letter-spacing:.3px}
.mainnav a.active{color:var(--gold)}
.hero{position:absolute;top:96px;left:0;width:792px;height:350px;background:var(--hero)}
.hero-photo{position:absolute;left:420px;top:0;width:290px;height:350px;background:radial-gradient(ellipse at 55% 45%,#8a5a40 0%,#5a3a2c 45%,var(--hero) 80%)}
.hero-copy{position:absolute;left:136px;top:58px;font-family:"Questrial",sans-serif;line-height:1}
.hero-copy .l1{font-size:42px;color:var(--ink)}
.hero-copy .l2{font-size:32px;color:var(--ink);margin-top:7px}
.hero-copy .l3{font-size:32px;color:var(--gold);margin-top:9px}
.btn{display:inline-block;border:1.5px solid var(--gold);color:var(--ink);font-family:"Questrial",sans-serif;font-size:11px;letter-spacing:.5px;text-align:center}
.hero .btn{position:absolute;left:138px;top:236px;width:96px;height:25px;line-height:22px}
.arrow{position:absolute;top:120px;width:64px;height:64px;border-radius:50%;background:rgba(255,255,255,.08)}
.arrow svg{position:absolute;left:13px;top:13px}
.arrow.prev{left:28px}.arrow.next{left:701px}
.band{position:absolute;top:446px;left:0;width:792px;height:204px;background:var(--tan)}
.products{position:absolute;top:401px;left:135px;display:flex;gap:18px}
.product{width:117px;height:117px;border-radius:50%;background:var(--white);position:relative}
.product i{position:absolute;left:30px;top:18px;width:56px;height:80px;display:block}
.band .btn{position:absolute;left:324px;top:82px;width:144px;height:24px;line-height:21px;border-color:#3a2c22;color:#2b2018;font-size:10.5px}
.band p{position:absolute;left:140px;top:120px;width:512px;text-align:center;font-weight:300;font-size:11.3px;line-height:20.5px;color:#fbf3ea}
.feature{position:absolute;top:650px;left:0;width:792px;height:298px;background:radial-gradient(ellipse at 72% 40%,var(--green-light) 0%,var(--green-mid) 40%,var(--green-deep) 90%)}
.panel{position:absolute;left:95px;top:16px;width:602px;height:266px;background:var(--panel)}
.panel h2{position:absolute;left:30px;top:22px;width:520px;font-family:"Questrial",sans-serif;font-weight:400;font-size:20.5px;line-height:28px}
.panel ul{position:absolute;left:28px;top:90px;list-style:none}
.panel li{font-size:10.6px;height:21.7px;display:flex;align-items:center;gap:6px}
.panel li svg{flex:none}
.cover{position:absolute;left:462px;top:56px;width:82px;height:104px;background:linear-gradient(160deg,#f2f6e8,#9fcf5a 60%,#4f8a2a)}
.panel .btn{position:absolute;left:453px;top:193px;width:103px;height:29px;line-height:26px;border-color:var(--white);font-size:11px}
.seen{position:absolute;top:948px;left:0;width:792px;height:107px;background:var(--white);color:#1a1a1a;text-align:center}
.seen h3{font-family:"Questrial",sans-serif;font-weight:400;font-size:21px;margin-top:13px}
.outlets{position:absolute;top:56px;left:112px;width:570px;display:flex;align-items:center;justify-content:space-between}
.outlets span{font-family:"Questrial",sans-serif;font-size:20px;color:#333}
.footer{position:absolute;top:1055px;left:0;width:792px;height:145px;background:var(--footer)}
.fcol{position:absolute;top:19px}
.fcol h4{font-family:"Questrial",sans-serif;font-weight:400;font-size:14px;margin-bottom:7px}
.fcol a{display:block;font-size:10.4px;color:var(--ink);text-decoration:none;line-height:20px}
.fcol a span{display:inline-block;width:13px;height:13px;border-radius:50%;background:var(--white);vertical-align:-3px;margin-right:9px}
.copy-base{position:absolute;left:220px;top:110px;width:352px;height:70px;border-radius:50%;background:#333}
.copyright{position:absolute;top:121px;left:0;width:792px;text-align:center;font-size:9.5px}
</style>
</head>
<body>
<header class="topbar">
  <div class="brand">TQ BARLOW</div>
  <div class="social" aria-label="Social links"><span></span><span></span><span></span><span></span></div>
</header>
<nav class="mainnav">
  <a class="active" href="#">HOME</a><a href="#">ABOUT</a><a href="#">PRODUCTS</a><a href="#">BLOG</a><a href="#">SUCCESS ROOM</a><a href="#">FORUM</a><a href="#">MEDIA ROOM</a>
</nav>
<section class="hero">
  <div class="hero-photo" role="img" aria-label="Portrait of a woman with long curly auburn hair"></div>
  <div class="hero-copy">
    <div class="l1">DISCOVER</div>
    <div class="l2">SECRETS TO A</div>
    <div class="l3">SLIMMER, SEXIER</div>
    <div class="l3">&amp; HEALTHIER YOU</div>
  </div>
  <a class="btn">READ MORE</a>
  <div class="arrow prev"><svg width="38" height="38"><circle cx="19" cy="19" r="19" fill="#8a8a8a"/><path d="M22 12l-7 7 7 7" stroke="#4a4a4a" stroke-width="1.5" fill="none"/></svg></div>
  <div class="arrow next"><svg width="38" height="38"><circle cx="19" cy="19" r="19" fill="#8a8a8a"/><path d="M16 12l7 7-7 7" stroke="#4a4a4a" stroke-width="1.5" fill="none"/></svg></div>
</section>
<section class="band">
  <a class="btn">VIEW ALL PRODUCTS</a>
  <p>TQ Barlow is a nutritionist and certified weight-loss expert, passionate relationship/life coach, and inspirational speaker. She has been featured on The Dale Monroe Morning Show, The Carla Benning Show, The Reggie Lane Show, and The Marcus Holt Show.</p>
</section>
<div class="products">
  <div class="product"><i role="img" aria-label="Green smoothie book cover" style="background:linear-gradient(160deg,#eef5e0,#8fc552)"></i></div>
  <div class="product"><i role="img" aria-label="Weight loss book cover" style="background:linear-gradient(160deg,#f7d6e6,#e04a94)"></i></div>
  <div class="product"><i role="img" aria-label="Belly fat book cover" style="background:linear-gradient(160deg,#f4f4f4,#d9574a)"></i></div>
  <div class="product"><i role="img" aria-label="Look and feel younger program box" style="background:linear-gradient(160deg,#fbe7ef,#e07aa0)"></i></div>
</div>
<section class="feature" role="img" aria-label="Green smoothie glass with cucumber and parsley">
  <div class="panel">
    <h2>The 10-Day Green Blend Reset: Lose Up to 15 Pounds in 10 Days!</h2>
    <ul>
      <li><svg width="22" height="18"><path d="M2 9l6 6L20 2" stroke="var(--tick)" stroke-width="4" fill="none"/></svg>Lose 10-15 pounds in 10 days</li>
      <li><svg width="22" height="18"><path d="M2 9l6 6L20 2" stroke="var(--tick)" stroke-width="4" fill="none"/></svg>Get rid of stubborn body fat, including belly fat</li>
      <li><svg width="22" height="18"><path d="M2 9l6 6L20 2" stroke="var(--tick)" stroke-width="4" fill="none"/></svg>Drop pounds and inches fast, without grueling workouts</li>
      <li><svg width="22" height="18"><path d="M2 9l6 6L20 2" stroke="var(--tick)" stroke-width="4" fill="none"/></svg>Learn to live a healthier lifestyle of detoxing and healthy eating</li>
      <li><svg width="22" height="18"><path d="M2 9l6 6L20 2" stroke="var(--tick)" stroke-width="4" fill="none"/></svg>Help your body naturally crave healthy foods so you never have to diet again</li>
      <li><svg width="22" height="18"><path d="M2 9l6 6L20 2" stroke="var(--tick)" stroke-width="4" fill="none"/></svg>Receive over 100 green smoothie recipes for various health conditions and goals</li>
    </ul>
    <div class="cover" role="img" aria-label="Green blend reset book cover"></div>
    <a class="btn">Available Now</a>
  </div>
</section>
<section class="seen">
  <h3>As Seen On</h3>
  <div class="outlets">
    <svg width="14" height="18"><path d="M11 2L4 9l7 7" stroke="#222" stroke-width="3" fill="none"/></svg>
    <span>NBT</span><span>KVX</span><span>RADIANCE.com</span><span>WAVE</span><span>Home Circle</span>
    <svg width="14" height="18"><path d="M3 2l7 7-7 7" stroke="#222" stroke-width="3" fill="none"/></svg>
  </div>
</section>
<footer class="footer">
  <div class="fcol" style="left:98px"><h4>ABOUT US</h4><a>Company Info</a><a>Services</a><a>Clients</a></div>
  <div class="fcol" style="left:226px"><h4>ADVICE</h4><a>FAQ</a><a>Solutions</a><a>Contacts</a></div>
  <div class="fcol" style="left:356px"><h4>ADVICE</h4><a>Privacy Policy</a><a>Disclaimer</a><a>Terms of Use</a></div>
  <div class="fcol" style="left:500px"><h4>JOIN IN</h4><a>Sign Up</a><a>Forums</a><a>Promotions</a></div>
  <div class="fcol" style="left:611px"><h4>FOLLOW US</h4><a><span></span>Friendline</a><a><span></span>Chirpline</a></div>
  <div class="copy-base"></div>
  <div class="copyright">Copyright © 2014 TQ Barlow. All Rights Reserved</div>
</footer>
</body>
</html>
```